Box Design of "pet rapid test for dogs & cats" with professional use

"The market is in Southeast Asia, South America, Europe, and the U.S."
Clients: Veterinary clinics, pet hospitals,(a small number of home use)

Primary colors:
Orange, Green,or Blue, (select 1,or 2 color)
Neutrals: Black, Gray, or White (optional)
Dimensions:135mm(L)*90mm(W)*105mm(W)

Kindly review the attached file for additional content
Updates

I have increased my budget, please provide a satisfactory design solution, thank you very much for your work.

Target Market(s)

Southeast Asia, South America, Europe, and the U.S.

Industry/Entity Type

Veterinary test kit for dogs & cats

Colors
0054AA
0677BA
7BADD7
CADEEF
E8F1F8
0094D4
00A9DD
6FCCEA
C7EBF8
E9F6FB
00AB8E
00BBA5
67D7C9
C6EFE9
E9F9F6
59FF00
82FF00
B8FF75
E3FFCB
F4FFEA
F0912C
F2A743
F7CA91
FBE8D2
FDF5EE
EE7325
F08F49
F5BC92
FAE3D3
FDF4ED

Requirements
Nice to have
• Appealing Box Appearance with professional

```html
<!DOCTYPE html>
<html lang="en">
<head>
<meta charset="UTF-8">
<title>VETORA Pet Rapid Test Kit – Box Dieline</title>
<link href="https://fonts.googleapis.com/css2?family=Archivo:wght@400;600;800&display=swap" rel="stylesheet">
<style>
  :root{
    --navy-top:#30597c;
    --navy-bottom:#263a51;
    --white:#ffffff;
    --label:#f2f4f3;
    --ink:#1b2430;
    --fold:rgba(255,255,255,.9);
  }
  *{margin:0;padding:0;box-sizing:border-box}
  html,body{width:1200px;height:780px;overflow:hidden;background:#fff}
  body{font-family:"Archivo",Arial,sans-serif;color:var(--white)}
  .canvas{position:relative;width:1200px;height:780px;background:#fff}
  .dieline{position:absolute;left:0;top:0}
  .abs{position:absolute;white-space:nowrap}

  .brand-name{font-weight:800;font-size:10px;letter-spacing:.2px}
  .brand-mark{display:inline-block;width:7px;height:7px;border-radius:50%;background:var(--white);margin-right:4px;vertical-align:1px}
  .brand-tag{font-size:3.4px;letter-spacing:.3px;line-height:1.2}
  .title-main{font-weight:800;font-size:14px;letter-spacing:.3px}
  .title-sub{font-weight:600;font-size:9.5px;letter-spacing:.2px}
  .title-note{font-weight:400;font-size:7.2px;letter-spacing:.2px}
  .animals{position:absolute;border-radius:40px 40px 6px 6px;background:linear-gradient(180deg,rgba(255,255,255,.92),rgba(255,255,255,.78))}

  .info-band{position:absolute;background:var(--white);height:30px;top:455px}
  .icon-row{position:absolute;top:455px;height:30px;display:flex;align-items:center}
  .ivd{border:1.4px solid var(--ink);color:var(--ink);font-weight:800;font-size:9px;padding:0 2px;line-height:11px}
  .count{display:flex;flex-direction:column;align-items:center;color:var(--ink)}
  .count b{background:var(--ink);color:var(--white);font-size:7px;font-weight:800;width:29px;text-align:center;line-height:9px}
  .count span{font-size:3.8px;font-weight:800;letter-spacing:.5px;margin-top:1px}

  .contents{position:absolute;font-size:6.2px;line-height:1.3}
  .contents li{list-style:none;display:flex;gap:5px;align-items:flex-start}
  .tick{width:8px;height:8px;flex:none}

  .side-name{font-weight:800;font-size:20px;letter-spacing:.4px;text-align:center}
  .side-tag{font-size:7px;letter-spacing:.2px;text-align:center}
  .label-area{position:absolute;left:453px;top:396px;width:148px;height:94px;border:1px dashed var(--white);padding:3px}
  .label-area div{width:100%;height:100%;background:var(--label)}

  .details{position:absolute;left:914px;top:350px;width:142px;font-size:4.5px;line-height:1.38}
  .details h3{font-weight:800;font-size:4.8px}
  .details .head{font-weight:800;padding-left:6px}
  .details .sub{padding-left:20px}
  .details p{margin:0}
  .maker{position:absolute;left:938px;top:516px;width:100px;text-align:center}
  .maker .by{font-size:4.6px;font-weight:800}
  .maker .tag{font-size:2.6px;letter-spacing:.8px;opacity:.85}
</style>
</head>
<body>
<div class="canvas">

  <svg class="dieline" width="1200" height="780" viewBox="0 0 1200 780" aria-hidden="true">
    <defs>
      <linearGradient id="boardFill" x1="0" y1="0" x2="0" y2="1" gradientUnits="userSpaceOnUse" gradientTransform="translate(0,100) scale(1,580)">
        <stop offset="0" stop-color="var(--navy-top)"/>
        <stop offset="1" stop-color="var(--navy-bottom)"/>
      </linearGradient>
    </defs>
    <g fill="url(#boardFill)" stroke="rgba(255,255,255,.55)" stroke-width="0.8" stroke-dasharray="4 3">
      <path class="glue-flap" d="M170 334 L137 336 Q130 336 130 343 L130 530 Q130 537 137 537 L170 540 Z"/>
      <path class="panel-front" d="M170 331 L170 125 Q170 110 185 110 L426 110 Q441 110 441 125 L441 672 L395 672 Q382 672 382 659 L382 632 L230 632 L230 659 Q230 672 217 672 L170 672 Z"/>
      <path class="panel-side" d="M441 331 L447 325 L447 260 Q447 250 457 250 L600 250 Q612 250 613 262 L617 312 L622 325 L622 642 L540 642 Q532 642 532 634 L532 603 L441 541 Z"/>
      <path class="panel-back" d="M622 331 L894 331 L894 541 L832 632 L832 660 Q832 672 820 672 L695 672 Q683 672 683 660 L683 632 L622 541 Z"/>
      <path class="panel-info" d="M894 331 L900 325 L904 312 L904 262 Q906 250 918 250 L1069 250 L1069 325 L1074 331 L1074 541 L984 603 L984 634 Q984 642 976 642 L894 642 Z"/>
    </g>
    <g class="folds" stroke="var(--fold)" stroke-width="0.9" stroke-dasharray="6 4" fill="none">
      <line x1="170" y1="150" x2="441" y2="150"/>
      <line x1="170" y1="331" x2="1074" y2="331"/>
      <line x1="170" y1="541" x2="1074" y2="541"/>
      <line x1="170" y1="331" x2="170" y2="541"/>
      <line x1="441" y1="331" x2="441" y2="541"/>
      <line x1="622" y1="331" x2="622" y2="541"/>
      <line x1="894" y1="331" x2="894" y2="541"/>
    </g>
  </svg>

  <!-- Front panel (English) -->
  <div class="abs brand-name" style="left:182px;top:372px"><span class="brand-mark"></span>VETORA</div>
  <div class="abs brand-tag" style="left:183px;top:385px">LOVED BY PETS, TRUSTED BY VETS</div>
  <div class="abs title-main" style="left:182px;top:399px">PET RAPID</div>
  <div class="abs title-sub" style="left:182px;top:416px">TEST KIT</div>
  <div class="abs title-note" style="left:182px;top:428px">FOR DOGS &amp; CATS</div>
  <div class="animals" role="img" aria-label="White silhouettes of a standing dog and a cat" style="left:278px;top:384px;width:155px;height:62px"></div>

  <div class="info-band" style="left:130px;width:311px"></div>
  <div class="icon-row" style="left:203px;gap:0">
    <span class="ivd">IVD</span>
    <svg width="30" height="22" viewBox="0 0 30 22" style="margin-left:12px" aria-label="Storage 2–30°C" role="img">
      <line x1="14" y1="3" x2="14" y2="18" stroke="var(--ink)" stroke-width="1.2"/><circle cx="14" cy="18.5" r="1.6" fill="var(--ink)"/>
      <text x="16" y="6" font-size="4" fill="var(--ink)" font-family="Archivo">30°C</text><text x="4" y="14" font-size="4" fill="var(--ink)" font-family="Archivo">2°C</text>
    </svg>
    <svg width="18" height="20" viewBox="0 0 18 20" style="margin-left:5px" aria-label="Keep away from sunlight" role="img">
      <circle cx="9" cy="7" r="2.4" fill="var(--ink)"/><g stroke="var(--ink)" stroke-width=".8"><line x1="9" y1="1" x2="9" y2="3"/><line x1="3" y1="7" x2="5" y2="7"/><line x1="13" y1="7" x2="15" y2="7"/><line x1="5" y1="3" x2="6.3" y2="4.3"/><line x1="13" y1="3" x2="11.7" y2="4.3"/><line x1="4" y1="13" x2="9" y2="10"/><line x1="14" y1="13" x2="9" y2="10"/></g><rect x="7.5" y="14" width="3" height="4" fill="var(--ink)"/>
    </svg>
    <svg width="16" height="14" viewBox="0 0 16 14" style="margin-left:9px" aria-label="Read instructions" role="img">
      <path d="M1 2 L7.5 3 L7.5 13 L1 12 Z M14.5 2 L8.5 3 L8.5 13 L14.5 12 Z" fill="none" stroke="var(--ink)" stroke-width=".9"/><text x="10" y="10.5" font-size="7" font-weight="800" fill="var(--ink)" font-family="Archivo">i</text>
    </svg>
    <svg width="18" height="18" viewBox="0 0 18 18" style="margin-left:23px" aria-label="Do not reuse" role="img">
      <circle cx="9" cy="9" r="7.8" fill="none" stroke="var(--ink)" stroke-width="1.1"/><line x1="3.5" y1="14.5" x2="14.5" y2="3.5" stroke="var(--ink)" stroke-width="1.1"/><text x="5.6" y="12" font-size="8" fill="var(--ink)" font-family="Archivo">2</text>
    </svg>
    <div class="count" style="margin-left:30px"><b>10</b><span>TESTS/BOX</span></div>
  </div>

  <ul class="contents" style="left:191px;top:496px">
    <li><svg class="tick" viewBox="0 0 10 10"><rect x=".6" y=".6" width="8.4" height="8.4" rx="1.5" fill="none" stroke="#fff" stroke-width=".9"/><path d="M2.6 5 L4.4 6.8 L9.4 1.5" fill="none" stroke="#fff" stroke-width=".9"/></svg>Test Kits(Cassette,disposable dropper,desiccant)</li>
  </ul>
  <ul class="contents" style="left:191px;top:514px">
    <li><svg class="tick" viewBox="0 0 10 10"><rect x=".6" y=".6" width="8.4" height="8.4" rx="1.5" fill="none" stroke="#fff" stroke-width=".9"/><path d="M2.6 5 L4.4 6.8 L9.4 1.5" fill="none" stroke="#fff" stroke-width=".9"/></svg>Assay buffer</li>
  </ul>
  <div class="abs contents" style="left:205px;top:528px">Store at 2~30°C,Avoid direct sunlight</div>
  <ul class="contents" style="left:349px;top:496px">
    <li><svg class="tick" viewBox="0 0 10 10"><rect x=".6" y=".6" width="8.4" height="8.4" rx="1.5" fill="none" stroke="#fff" stroke-width=".9"/><path d="M2.6 5 L4.4 6.8 L9.4 1.5" fill="none" stroke="#fff" stroke-width=".9"/></svg>Sterile swabs</li>
  </ul>
  <ul class="contents" style="left:349px;top:514px">
    <li><svg class="tick" viewBox="0 0 10 10"><rect x=".6" y=".6" width="8.4" height="8.4" rx="1.5" fill="none" stroke="#fff" stroke-width=".9"/><path d="M2.6 5 L4.4 6.8 L9.4 1.5" fill="none" stroke="#fff" stroke-width=".9"/></svg>Instruction manual</li>
  </ul>

  <!-- Side panel -->
  <div class="abs side-name" style="left:441px;width:181px;top:346px">VETORA</div>
  <div class="abs side-tag" style="left:441px;width:181px;top:371px">LOVED BY PETS, TRUSTED BY VETS</div>
  <div class="label-area"><div></div></div>

  <!-- Back panel (Spanish) -->
  <div class="abs brand-name" style="left:635px;top:372px"><span class="brand-mark"></span>VETORA</div>
  <div class="abs brand-tag" style="left:636px;top:385px">QUERIDO POR LAS MASCOTAS<br>CONFIADO POR VETERINARIOS</div>
  <div class="abs title-main" style="left:635px;top:399px">KIT DE PRUEBA</div>
  <div class="abs title-sub" style="left:635px;top:417px;font-size:8px">RÁPIDA PARA MASCOTAS</div>
  <div class="abs title-note" style="left:635px;top:428px">PERROS Y GATOS</div>
  <div class="animals" role="img" aria-label="White silhouettes of a standing dog and a cat" style="left:744px;top:388px;width:142px;height:58px"></div>

  <div class="info-band" style="left:622px;width:272px"></div>
  <div class="icon-row" style="left:656px">
    <span class="ivd">IVD</span>
    <svg width="30" height="22" viewBox="0 0 30 22" style="margin-left:12px" aria-label="Almacenamiento 2–30°C" role="img">
      <line x1="14" y1="3" x2="14" y2="18" stroke="var(--ink)" stroke-width="1.2"/><circle cx="14" cy="18.5" r="1.6" fill="var(--ink)"/>
      <text x="16" y="6" font-size="4" fill="var(--ink)" font-family="Archivo">30°C</text><text x="4" y="14" font-size="4" fill="var(--ink)" font-family="Archivo">2°C</text>
    </svg>
    <svg width="18" height="20" viewBox="0 0 18 20" style="margin-left:5px" aria-label="Evitar la luz solar" role="img">
      <circle cx="9" cy="7" r="2.4" fill="var(--ink)"/><g stroke="var(--ink)" stroke-width=".8"><line x1="9" y1="1" x2="9" y2="3"/><line x1="3" y1="7" x2="5" y2="7"/><line x1="13" y1="7" x2="15" y2="7"/><line x1="5" y1="3" x2="6.3" y2="4.3"/><line x1="13" y1="3" x2="11.7" y2="4.3"/><line x1="4" y1="13" x2="9" y2="10"/><line x1="14" y1="13" x2="9" y2="10"/></g><rect x="7.5" y="14" width="3" height="4" fill="var(--ink)"/>
    </svg>
    <svg width="16" height="14" viewBox="0 0 16 14" style="margin-left:9px" aria-label="Leer instrucciones" role="img">
      <path d="M1 2 L7.5 3 L7.5 13 L1 12 Z M14.5 2 L8.5 3 L8.5 13 L14.5 12 Z" fill="none" stroke="var(--ink)" stroke-width=".9"/><text x="10" y="10.5" font-size="7" font-weight="800" fill="var(--ink)" font-family="Archivo">i</text>
    </svg>
    <svg width="18" height="18" viewBox="0 0 18 18" style="margin-left:23px" aria-label="No reutilizar" role="img">
      <circle cx="9" cy="9" r="7.8" fill="none" stroke="var(--ink)" stroke-width="1.1"/><line x1="3.5" y1="14.5" x2="14.5" y2="3.5" stroke="var(--ink)" stroke-width="1.1"/><text x="5.6" y="12" font-size="8" fill="var(--ink)" font-family="Archivo">2</text>
    </svg>
    <div class="count" style="margin-left:30px"><b>10</b><span>PRUEBAS</span></div>
  </div>

  <ul class="contents" style="left:643px;top:496px">
    <li><svg class="tick" viewBox="0 0 10 10"><rect x=".6" y=".6" width="8.4" height="8.4" rx="1.5" fill="none" stroke="#fff" stroke-width=".9"/><path d="M2.6 5 L4.4 6.8 L9.4 1.5" fill="none" stroke="#fff" stroke-width=".9"/></svg><span>Kits de prueba (cassette, gotero desechable<br>desecante)</span></li>
  </ul>
  <ul class="contents" style="left:643px;top:514px">
    <li><svg class="tick" viewBox="0 0 10 10"><rect x=".6" y=".6" width="8.4" height="8.4" rx="1.5" fill="none" stroke="#fff" stroke-width=".9"/><path d="M2.6 5 L4.4 6.8 L9.4 1.5" fill="none" stroke="#fff" stroke-width=".9"/></svg>Buffer de ensayo</li>
  </ul>
  <div class="abs contents" style="left:657px;top:528px">Almacenamiento: 2~30°C</div>
  <ul class="contents" style="left:802px;top:496px">
    <li><svg class="tick" viewBox="0 0 10 10"><rect x=".6" y=".6" width="8.4" height="8.4" rx="1.5" fill="none" stroke="#fff" stroke-width=".9"/><path d="M2.6 5 L4.4 6.8 L9.4 1.5" fill="none" stroke="#fff" stroke-width=".9"/></svg>Hisopos estériles</li>
  </ul>
  <ul class="contents" style="left:802px;top:514px">
    <li><svg class="tick" viewBox="0 0 10 10"><rect x=".6" y=".6" width="8.4" height="8.4" rx="1.5" fill="none" stroke="#fff" stroke-width=".9"/><path d="M2.6 5 L4.4 6.8 L9.4 1.5" fill="none" stroke="#fff" stroke-width=".9"/></svg>Manual de instrucciones</li>
  </ul>

  <!-- Info panel -->
  <div class="details">
    <h3>VETORA<br>RAPID TEST KIT</h3>
    <p style="margin-top:4px">Simple &amp; Convenient:no professional skills required,Simple enough for home use.</p>
    <p class="head">☑ FÁCILYPRÁCTICO:</p>
    <p class="sub">✔ Sin capacitación previa</p>
    <p class="sub">✔ Suficientemente simple para Para uso en casa</p>
    <p>Fast &amp; Efficient: Digital results in &lt; 10 minutes- from start to completion.</p>
    <p class="head">☑ RÁPIDOYEFICIENTE:</p>
    <p class="sub">✔ Resultados digitales en &lt;10 minutos</p>
    <p class="sub">✔ Desdeinicio hasta resultado final</p>
    <p>Accurate &amp; Reliable:Quick and trustworthy pet health results using advanced lateral flow biotech,Trusted by vet clinics worldwide.</p>
    <p class="head">☑ PRECISOYFIABLE:</p>
    <p class="sub">✔ Resultados rápidos y confiables con tecnología de inmunocromatografía avanzada</p>
    <p class="sub">✔ Validado por clínicas veterinarias a nivel global</p>
    <p>Supports screening of multiple diseases, Helping pet owners detect issues early.</p>
    <p class="head">☑ DETECCIÓNMULTIENFERMEDADES:</p>
    <p class="sub">✔ Evalúa múltiples patologías simultáneamente</p>
    <p class="sub">✔ Ayudaralosdueñosde mascotas a detectar problemas a tiempo</p>
  </div>
  <div class="maker">
    <div class="by">MADE by ORVELIX</div>
    <div class="tag">LOVED BY PETS, TRUSTED BY VET</div>
  </div>

</div>
</body>
</html>
```